Ebook Cover Design for Coif PaNORAma!

I wrote a three-part series based on my year in beauty school as a more mature student (34yo as opposed to the mostly 20yo crowd). It's called Coif PaNORAma, based on the blog of the same name that I kept the entire year. While there, I won many competitions, I was on student council, my mom passed away from cancer, and I traveled to Washington, D.C., to speak to Senate Hall about colon cancer research and prevention (for my mom). It's got a bit of everything. The book is considered a work of narrative nonfiction or creative nonfiction. Basically, it's a memoir.

The three titles are:

Coif PaNORAma: Frayed Tips
Coif PaNORAma: Lather Once More
Coif PaNORAma: A Quiet Braid

So, three book covers altogether. Different colors but same theme.

(My name is NORA, hence the clever title. Heh.)

Am willing to consider not using a colon after "PaNORAma."

Also, the way it's spelled...Coif PaNORAma...it's important to keep that capitalization because of my name in the word "PaNORAma."

My pseudonym is Nora Bellwyn. That should, of course, be included on the cover.

The cover should meet the specs required for uploading to Quillmart and Pagevault.

Thanks for your ideas! x
Updates

I want to make it clear I am looking for the first cover only at this point for Coif PaNORAma: Frayed Tips (Frayed Tips is the subtitle).My author name is Nora Bellwyn. Very important! Added Saturday, October 11, 2014

Project Deadline Extended Reason: I have been busy volunteering for a political campaign while also doing my day job. I appreciate the submissions thus far! x Added Sunday, October 19, 2014

Project Deadline Extended Reason: I was involved with a political campaign that took up a lot of my time unexpectedly in the end. Extending deadline for this reason! x Added Tuesday, November 11, 2014

Target Market(s)

Teen to adult women. It reads like chick lit.

Industry/Entity Type

School

Font styles to use
Decorative

Requirements
Must have
• My name "Nora" must stand out somehow in the word "PaNORAma."
Nice to have
• Cosmetology related items, like blow dryer, shears (hair cutting scissors), combs, etc.
Should not have
• No red, white and blue themes. No blue cancer ribbons. Just hair-related items.

```html
<!DOCTYPE html>
<html lang="en">
<head>
<meta charset="utf-8">
<title>Coif PaNORAma: Frayed Tips — Cover</title>
<link rel="stylesheet" href="https://fonts.googleapis.com/css2?family=Bowlby+One&family=Fascinate&family=Montserrat:wght@400&display=swap">
<style>
  :root {
    --paper: #ffffff;
    --ink: #000000;
    --hot-pink: #ef1a8a;
    --cream: #f1dccb;
    --hair-deep: rgba(70, 8, 14, 0.95);
    --hair-mid: rgba(128, 28, 36, 0.9);
    --hair-light: rgba(176, 74, 82, 0.75);
    --skin: rgba(232, 214, 206, 0.85);
    --author: #f4f4f4;
  }
  * { margin: 0; padding: 0; box-sizing: border-box; }
  html, body {
    width: 813px;
    height: 1200px;
    overflow: hidden;
    background: var(--paper);
  }
  .cover {
    position: absolute;
    left: 25px;
    top: 25px;
    width: 763px;
    height: 1140px;
    background: var(--ink);
    overflow: hidden;
  }
  .hero-photo {
    position: absolute;
    inset: 0;
    background:
      radial-gradient(ellipse 90px 220px at 40px 300px, var(--skin), transparent 85%),
      radial-gradient(ellipse 150px 110px at 300px 1000px, rgba(225, 200, 192, 0.6), transparent 80%),
      radial-gradient(ellipse 180px 140px at 260px 180px, var(--hair-light), transparent 80%),
      radial-gradient(ellipse 160px 150px at 380px 420px, var(--hair-light), transparent 80%),
      radial-gradient(ellipse 190px 160px at 200px 700px, var(--hair-light), transparent 80%),
      radial-gradient(ellipse 150px 120px at 360px 860px, rgba(176, 74, 82, 0.55), transparent 80%),
      radial-gradient(ellipse 300px 260px at 230px 260px, var(--hair-mid), transparent 85%),
      radial-gradient(ellipse 280px 300px at 300px 620px, var(--hair-mid), transparent 85%),
      radial-gradient(ellipse 260px 220px at 230px 930px, var(--hair-mid), transparent 85%),
      radial-gradient(ellipse 340px 560px at 220px 560px, var(--hair-deep), transparent 100%);
  }
  .title-block {
    position: absolute;
    left: 119px;
    top: 416px;
    width: 620px;
    font-weight: 400;
  }
  .series-name {
    display: block;
    font-family: "Bowlby One", sans-serif;
    color: var(--hot-pink);
    line-height: 0.95;
    letter-spacing: 2px;
  }
  .series-name .line-one { display: block; font-size: 72px; }
  .series-name .line-two { display: block; font-size: 84px; }
  .series-name .name-highlight {
    text-decoration: underline;
    text-decoration-thickness: 5px;
    text-underline-offset: 8px;
  }
  .subtitle {
    display: block;
    margin-top: 16px;
    font-family: "Fascinate", serif;
    font-size: 84px;
    color: var(--cream);
    letter-spacing: 2px;
    line-height: 1;
  }
  .shears-icon {
    position: absolute;
    left: 615px;
    top: 419px;
    width: 98px;
    height: 90px;
  }
  .author {
    position: absolute;
    right: 24px;
    top: 1078px;
    font-family: "Montserrat", sans-serif;
    font-size: 30px;
    color: var(--author);
    letter-spacing: 0.3px;
  }
</style>
</head>
<body>
  <main class="cover">
    <div class="hero-photo" role="img" aria-label="Photo of a smiling woman tilting her head back, with voluminous curly red hair falling over her shoulder"></div>

    <h1 class="title-block">
      <span class="series-name">
        <span class="line-one">COIF</span>
        <span class="line-two">Pa<span class="name-highlight">NORA</span>ma</span>
      </span>
      <span class="subtitle">FRAYED TIPS</span>
    </h1>

    <svg class="shears-icon" viewBox="0 0 98 90" aria-hidden="true">
      <g fill="none" stroke="var(--hot-pink)" stroke-width="6" stroke-linecap="round">
        <line x1="30" y1="8" x2="64" y2="48"/>
        <line x1="4" y1="58" x2="64" y2="40"/>
        <circle cx="78" cy="30" r="11"/>
        <circle cx="74" cy="66" r="11"/>
      </g>
    </svg>

    <p class="author">Nora Bellwyn</p>
  </main>
</body>
</html>
```